Poster for a Bicycle show/Expo

We need a poster for a Bicycle show/Expo and sustainable transport. Exhibitors will sell bikes, cycling clothing, accessories, etc. ...
This show is annual and the Poster is for the 2015 edition.

The style must be modern, dynamic, bright colors.

Your concept must be compatible in a landscape format. (We will ourselves adaptations of different formats.)
Width: 210 mm
Height: 297 mm
It's necessary for us to have the source file (vector) for make, later, the different format (flyers, website, ...)

Content of the Poster:
- 1 big picture (no clip art)
- Big title: « Foire Roulante » (« Salon » or « Salon du » can be small and « Vélo » big.)
- Subtitle: « et de la mobilité douce »
- Date: « 8, 9 et 10 mai 2015 » or « 8-10 mai 2015 »
- Place: « Halle TPV - Gare de Tavrel »
- Text line 1: « www.foire-roulante.ch - Entrée gratuite »
- Text line 2« Piste d’essais - Restauration sur place »
- Text line 3: « Ve 8 mai de 17h à 21h - Sa 9 mai de 10h à 20h - Di 10 mai de 10h à 18h »
- Please, leave a zone in the poster for sponsors logos
(The predominant information (most visible) are: « Foire Roulante » and « 8, 9 et 10 mai 2015 or 8-10 mai 2015 »)

Content of the big picture:
- from a cheap stock, like PixKopa.com
- a bicycle in action or a detail of a bicycle (or a accessory) (no race bike)
- a modern picture with bright colors.
- if a person is on the picture, we prefer a men
- not an aerial view with cyclists in a landscape.

Some examples of poster of shows - with typo-title worked

http://www.expobassinlumo.com/Temp/IMG/F_a7c2e9b4410d3f8a6e5b2c1d9f07e3a4b6c8d2e51907_200_296.png

http://qz4m.torvexpo.fr/Data/kmtorv_mer/block/F_8bd1c3e7720fa4b95e3d61c0a8f2e4b7d9c1a5f63e27b.pdf
(page 2 of this PDF)

http://salons.brivane-events.fr/images/brivane-events/foires-salons/phototheque/salon-auto-val-torbin/salon-auto-valtorbin2012-affiche.jpg

http://www.pralvo.net/blog/wp-content/uploads/2007/03/affiche-salon-du-livre.jpg

http://www.quilmora-gens.com/wp-content/affiche-festo-2007.jpg

Hello,

For information, for your next versions, please, add the text "Piste d'essais".

- Text line 1: « www.foire-roulante.ch - Entrée gratuite »
- Text line 2: « Piste d’essais - Restauration sur place »
- Text line 3: « Ve 8 mai de 17h à 21h - Sa 9 mai de 10h à 20h - Di 10 mai de 10h à 18h »

Thanks,
Olivier

Landscape

Sans Serif

```html
<!DOCTYPE html>
<html lang="fr">
<head>
<meta charset="utf-8">
<title>Foire Roulante 2015 – Affiche</title>
<link rel="stylesheet" href="https://fonts.googleapis.com/css2?family=Varela+Round&display=swap">
<style>
  :root {
    --backdrop: #efefef;
    --ink: #ffffff;
    --stone-light: #9a948a;
    --stone-mid: #6f6a62;
    --stone-dark: #3c3833;
    --pavement: #2a2827;
    --accent-red: #8e2a24;
  }
  html, body {
    margin: 0;
    width: 1200px;
    height: 900px;
    overflow: hidden;
    background: var(--backdrop);
  }
  .poster {
    position: absolute;
    left: 348px;
    top: 72px;
    width: 525px;
    height: 743px;
    overflow: hidden;
    font-family: "Varela Round", sans-serif;
    color: var(--ink);
    text-transform: uppercase;
  }
  .poster__photo {
    position: absolute;
    inset: 0;
    background:
      radial-gradient(ellipse at 25% 45%, rgba(142,42,36,0.35) 0 12%, transparent 30%),
      radial-gradient(ellipse at 45% 80%, rgba(142,42,36,0.25) 0 10%, transparent 35%),
      linear-gradient(180deg, var(--stone-mid) 0%, var(--stone-light) 30%, var(--stone-mid) 60%, var(--stone-dark) 82%, var(--pavement) 100%);
  }
  .poster__content {
    position: absolute;
    inset: 0;
    text-align: center;
  }
  .title {
    position: absolute;
    left: 0;
    right: 0;
    top: 62px;
    margin: 0;
    font-weight: 400;
    line-height: 1;
    letter-spacing: 2px;
  }
  .title__line { display: block; }
  .title__line--first { font-size: 128px; }
  .title__line--second { font-size: 90px; margin-top: 40px; }
  .subtitle {
    position: absolute;
    left: 0; right: 0;
    top: 430px;
    margin: 0;
    font-size: 18px;
    font-weight: 400;
  }
  .divider {
    position: absolute;
    left: 92px;
    top: 476px;
  }
  .info {
    position: absolute;
    left: 0; right: 0;
    margin: 0;
    font-weight: 400;
    white-space: nowrap;
  }
  .info--date { top: 520px; font-size: 18px; }
  .info--place { top: 560px; font-size: 18px; }
  .info--extras { top: 607px; font-size: 14px; }
  .info--hours { top: 651px; font-size: 12.5px; }
</style>
</head>
<body>
  <article class="poster">
    <div class="poster__photo" role="img" aria-label="Photo d'un vélo de ville rouge avec panier en osier, garé contre un mur de pierre avec une fenêtre à barreaux rouge, une grille blanche et une ardoise de menu"></div>
    <div class="poster__content">
      <h1 class="title">
        <span class="title__line title__line--first">Foire</span>
        <span class="title__line title__line--second">Roulante</span>
      </h1>
      <p class="subtitle">Et de la mobilité douce</p>
      <svg class="divider" width="346" height="8" viewBox="0 0 346 8" aria-hidden="true">
        <line x1="0" y1="4" x2="346" y2="4" stroke="#ffffff" stroke-width="6" stroke-dasharray="28 12"/>
      </svg>
      <p class="info info--date">8th-10th mai, 2015.</p>
      <p class="info info--place">Gare de Tavrel, Halle TPV.</p>
      <p class="info info--extras">Restauration sur place - Entrée gratuite!</p>
      <p class="info info--hours">Ve 8 mai de 17h à 21h / Sa 9 mai de 10h à 20h / Di 10 mai de 10h à 18h</p>
    </div>
  </article>
</body>
</html>
```